Real Estate Acquisition Company Needs Business Card Design

Tellwyn Real Estate is in need of a business card design!

As a Real Estate Acquisition Company, Tellwyn Real Estate conducts mutually beneficial real estate transactions that actively consider the needs of the seller. At Tellwyn Real Estate we’re actively buying properties from those that see value in a direct transaction, but more importantly want reassurances that they, personally, are in integral part of it. Of course, it all starts with fair market value, but it doesn’t stop there. We’ve found the most success when we offer more. And with our deep experience in this industry, we’ve discovered that we have a lot to offer!

We already have a logo and brand guidelines that we've uploaded. Our final design should stay true to the guidelines. We are looking for a business card design that has two names (Ex. Jane Doe & John Doe) and contact information for each person- this way the company principals can share a card as they often do business as a team.
Updates

The criteria was unfortunately not met on most designs. We are looking for a card that has a layout for TWO names and respective contact information for each of the two people. Almost all designs only had a space for one name and one set of contact information.

Industry/Entity Type

Real Estate

Contact Information for Business Card

We are looking for a business card design that has two names (Ex. Jane Doe & John Doe) and each of their contact information- this way the company principals can share a card as they often do business as a team.

Font styles to use
Other font styles liked:
• Use Brand Guidelines

Requirements
Must have
• Please stay true to our Brand Guidelines for colours, fonts, and positioning of logo.

We require a layout for two names and respective contact information. The company principals work as a team and want a card that has both their information on it.

```html
<!DOCTYPE html>
<html lang="en">
<head>
<meta charset="utf-8">
<title>Tellwyn Real Estate – Business Card</title>
<link rel="stylesheet" href="https://fonts.googleapis.com/css2?family=Roboto:wght@300;400;500&family=Roboto+Condensed:wght@400&display=swap">
<style>
  :root {
    --navy-deep: #0e1a2b;
    --navy-band: #16233a;
    --gold: #f2b443;
    --white: #ffffff;
    --ink: #111827;
    --rule: #e3e6eb;
    --stage: #dfe2e7;
  }
  * { box-sizing: border-box; margin: 0; padding: 0; }
  html, body { width: 1200px; height: 1200px; overflow: hidden; }
  body { background: var(--stage); font-family: "Roboto", sans-serif; position: relative; }

  .card {
    position: absolute;
    left: 220px;
    width: 760px;
    height: 500px;
    border-radius: 14px;
    overflow: hidden;
  }

  /* Front side */
  .card-front { top: 60px; background: var(--navy-deep); }
  .front-band {
    position: absolute; left: 0; right: 0; top: 135px; height: 195px;
    background: var(--navy-band);
  }
  .front-rule { position: absolute; top: 224px; height: 3px; background: var(--gold); }
  .front-rule.left { left: 0; width: 130px; }
  .front-rule.right { right: 0; width: 175px; }
  .brand-front {
    position: absolute; left: 0; right: 0; top: 170px;
    text-align: center; color: var(--white); font-weight: 500;
  }
  .brand-front .brand-name { display: block; font-size: 78px; line-height: 1; letter-spacing: 1px; }
  .brand-front .brand-sub { display: block; font-size: 16px; letter-spacing: 3px; margin-top: 10px; }
  .front-url {
    position: absolute; left: 0; right: 0; top: 418px;
    text-align: center; color: var(--white);
    font-family: "Roboto Condensed", sans-serif; font-size: 27px; letter-spacing: 5px;
  }

  /* Back side */
  .card-back { top: 640px; background: var(--white); }
  .back-name-band {
    position: absolute; left: 0; right: 0; top: 0; height: 136px; background: var(--navy-band);
  }
  .back-title-band {
    position: absolute; left: 0; right: 0; top: 136px; height: 63px; background: var(--gold);
  }
  .principal { position: absolute; top: 0; width: 360px; height: 290px; }
  .principal.first { left: 0; }
  .principal.second { left: 380px; }
  .person-name {
    position: absolute; left: 82px; top: 80px;
    color: var(--white); font-weight: 300; font-size: 32px; letter-spacing: 4px;
    white-space: nowrap;
  }
  .person-title {
    position: absolute; left: 84px; top: 150px;
    font-family: "Roboto Condensed", sans-serif; font-size: 23px; color: var(--ink);
    white-space: nowrap;
  }
  .principal.second .person-name,
  .principal.second .person-title { left: 40px; }

  .contact-list { list-style: none; }
  .contact-item {
    position: absolute; left: 94px;
    font-weight: 500; font-size: 20px; line-height: 28px; color: var(--ink);
    white-space: nowrap;
  }
  .principal.second .contact-item { left: 52px; }
  .contact-icon {
    position: absolute; left: -38px; top: 4px; width: 22px; height: 22px;
    color: var(--gold);
  }
  .contact-icon.at { font-size: 24px; font-weight: 400; top: -2px; }
  .item-email { top: 218px; }
  .item-phone { top: 258px; }

  .back-divider {
    position: absolute; left: 56px; right: 56px; top: 302px; height: 1px; background: var(--rule);
  }
  .office-list .item-address { top: 318px; }
  .office-list .item-web { top: 446px; }

  .brand-back {
    position: absolute; right: 38px; top: 400px;
    color: var(--navy-band); font-weight: 500; text-align: right;
  }
  .brand-back .brand-name { display: block; font-size: 38px; line-height: 1; }
  .brand-back .brand-sub { display: block; font-size: 10px; letter-spacing: 1.5px; margin-top: 5px; }
</style>
</head>
<body>

<section class="card card-front" aria-label="Card front">
  <div class="front-band"></div>
  <div class="front-rule left"></div>
  <div class="front-rule right"></div>
  <div class="brand-front">
    <span class="brand-name">TELLWYN</span>
    <span class="brand-sub">REAL ESTATE INC.</span>
  </div>
  <p class="front-url">www.tellwynrealestate.com</p>
</section>

<section class="card card-back" aria-label="Card back">
  <div class="back-name-band"></div>
  <div class="back-title-band"></div>

  <div class="principal first">
    <h1 class="person-name">John Doe</h1>
    <p class="person-title">EXECUTIVE DIRECTOR</p>
    <ul class="contact-list">
      <li class="contact-item item-email">
        <span class="contact-icon at">@</span>johndoe@tellwyn.com
      </li>
      <li class="contact-item item-phone">
        <svg class="contact-icon" viewBox="0 0 24 24" fill="currentColor" aria-hidden="true">
          <path d="M6.6 10.8a15.2 15.2 0 0 0 6.6 6.6l2.2-2.2c.3-.3.7-.4 1-.2 1.1.4 2.3.6 3.6.6.6 0 1 .4 1 1V20c0 .6-.4 1-1 1A17 17 0 0 1 3 4c0-.6.4-1 1-1h3.5c.6 0 1 .4 1 1 0 1.3.2 2.5.6 3.6.1.3 0 .7-.2 1z"/>
        </svg>5550142207
      </li>
    </ul>
  </div>

  <div class="principal second">
    <h2 class="person-name">Jane Doe</h2>
    <p class="person-title">MANAGING DIRECTOR</p>
    <ul class="contact-list">
      <li class="contact-item item-email">
        <span class="contact-icon at">@</span>janedoe@tellwyn.com
      </li>
      <li class="contact-item item-phone">
        <svg class="contact-icon" viewBox="0 0 24 24" fill="currentColor" aria-hidden="true">
          <path d="M6.6 10.8a15.2 15.2 0 0 0 6.6 6.6l2.2-2.2c.3-.3.7-.4 1-.2 1.1.4 2.3.6 3.6.6.6 0 1 .4 1 1V20c0 .6-.4 1-1 1A17 17 0 0 1 3 4c0-.6.4-1 1-1h3.5c.6 0 1 .4 1 1 0 1.3.2 2.5.6 3.6.1.3 0 .7-.2 1z"/>
        </svg>5550142318
      </li>
    </ul>
  </div>

  <div class="back-divider"></div>

  <ul class="contact-list office-list">
    <li class="contact-item item-address">
      <svg class="contact-icon" viewBox="0 0 24 24" fill="currentColor" aria-hidden="true">
        <path d="M12 1.5a7 7 0 0 0-7 7c0 5.2 7 14 7 14s7-8.8 7-14a7 7 0 0 0-7-7zm0 9.7a2.7 2.7 0 1 1 0-5.4 2.7 2.7 0 0 1 0 5.4z"/>
      </svg>Alderline Tower 2<br>Suite 1410, 4820 Marrow Ave<br>Edmonton, AB<br>T5K2M4
    </li>
    <li class="contact-item item-web">
      <svg class="contact-icon" viewBox="0 0 24 24" fill="none" stroke="currentColor" stroke-width="1.6" aria-hidden="true">
        <circle cx="12" cy="12" r="9.5"/>
        <ellipse cx="12" cy="12" rx="4.2" ry="9.5"/>
        <path d="M2.5 12h19M4 7h16M4 17h16"/>
      </svg>www.brightmerestaffing.ca
    </li>
  </ul>

  <div class="brand-back">
    <span class="brand-name">TELLWYN</span>
    <span class="brand-sub">REAL ESTATE INC.</span>
  </div>
</section>

</body>
</html>
```